WP website design (Brime)

We need a wordpress design for an established auction and real estate company based in Tennessee. The winning design will incorporate a professional color scheme with company logo in a clean layout. The design needs to consider that this will be developed on a responsive theme. Colors are those that will highlight the logo.

Industry/Entity Type

Real Estate

Font styles to use
Sans Serif

Colors

Designer to choose colors to be used in the design.

Requirements
Must have
• Navigation: 1) Home - with auctions as content as seen at http://velnorbidhouse.com/ 2) Current Auctions 3) Past Auctions 4) Referrals 5) Why Auction 6) About Us 7) Contact Us

Header will have logo, contact info, Social icons (Facebook, Twitter, Youtube) and tagline "Bid Bold With Brime!' Slideshow (use stock real estate image for image) will be used either in header or content area.

Widgets: Email signup form, Upcoming Auctions, Register for Online Bidding text, testimonials

Footer will have contact info (below) smaller company logo, and the association logos attached.

```html
<!DOCTYPE html>
<html lang="en">
<head>
<meta charset="utf-8">
<title>Brime Realty &amp; Auction LLC</title>
<link rel="stylesheet" href="https://fonts.googleapis.com/css2?family=Arimo:wght@400;700&family=Open+Sans:wght@600;700&family=Tinos:wght@700&display=swap">
<style>
:root{
  --navy:#383c5c;
  --navy-text:#3c4068;
  --green:#6a8c3f;
  --green-dark:#55732f;
  --green-text:#6d9142;
  --ink:#222;
  --muted:#444;
  --card-line:#d6d6d6;
  --white:#fff;
}
*{box-sizing:border-box;margin:0;padding:0}
html,body{width:882px;height:1200px;overflow:hidden}
body{background:var(--navy);font-family:"Arimo",Arial,sans-serif;color:var(--ink);position:relative}
.page{position:absolute;left:74px;top:18px;width:735px;height:1102px;background:var(--white)}
.abs{position:absolute}

/* header */
.brand{left:10px;top:8px;display:flex;align-items:center;gap:8px}
.brand-mark{width:14px;height:14px;background:var(--green)}
.brand-name{font-weight:700;color:var(--green);font-size:26px;line-height:1}
.brand-sub{font-weight:700;color:var(--green);font-size:11px;margin-top:3px}
.firm{left:158px;top:10px;font-size:8px;color:var(--muted);writing-mode:vertical-rl;transform:rotate(180deg);letter-spacing:.5px}
.social{right:12px;top:11px;display:flex;align-items:center;gap:10px}
.social-label{font-size:15px;color:var(--ink)}
.social-square{width:30px;height:30px;border-radius:4px}
.sq-a{background:#3b5998}.sq-b{background:#45b0e3}.sq-c{background:#c4161c}
.contact{right:9px;top:53px;display:flex;align-items:center;gap:7px;font-size:12.5px}
.contact svg{display:block}

/* nav */
.nav{left:8px;top:84px;width:721px;height:37px;background:var(--green);border-radius:3px;display:flex;align-items:center}
.nav a{display:block;flex:none;color:var(--white);text-decoration:none;font-size:11px;text-transform:uppercase;white-space:nowrap;height:23px;line-height:23px;padding:0;border-right:1px solid var(--green-dark);text-align:center}
.nav a:last-child{border-right:0}
.nav a.active{background:var(--navy);border-right:0;margin-left:8px}
.nav .spacer{flex:none;width:20px;height:23px;border-right:1px solid var(--green-dark)}

/* hero */
.hero{left:9px;top:126px;width:719px;height:281px;background:linear-gradient(180deg,#d6e2ec 0%,#e9eff3 35%,#5b6a5b 55%,#4b6a2e 72%,#3d6220 100%)}
.tagline{left:9px;top:190px;width:272px;height:44px;background:rgba(40,40,45,.72);color:var(--white);font-size:24px;line-height:44px;padding-left:15px;white-space:nowrap}

/* main */
.welcome{left:9px;top:428px;font-family:"Open Sans",sans-serif;font-weight:700;font-size:19px;color:var(--green-text);white-space:nowrap}
.intro{left:11px;top:458px;width:470px;font-size:10.5px;line-height:15px}
.section-title{left:12px;top:500px;font-family:"Open Sans",sans-serif;font-weight:700;font-size:19px;color:var(--navy-text)}
.auction{left:12px;width:462px;height:168px;background:linear-gradient(#fafafa,#ececec);border:1px solid var(--card-line);border-radius:4px}
.auction-title{position:absolute;left:13px;top:14px;font-family:"Tinos",serif;font-weight:700;font-size:12.5px;text-transform:uppercase;white-space:nowrap}
.auction-photo{position:absolute;left:14px;top:39px;width:132px;height:82px;border:2px solid #ddd;background:linear-gradient(180deg,#9cb8cf 0%,#cfc7b0 40%,#5a8f7e 55%,#3b3a45 100%)}
.auction-body{position:absolute;left:157px;top:39px;width:296px;font-size:10.5px;line-height:13px}
.auction-kind{color:var(--green-text);font-weight:700;font-size:11px;margin-bottom:5px}
.auction-body p{margin-bottom:7px}
.auction-body b{color:var(--navy-text)}
.auction-links{position:absolute;left:19px;top:131px;display:flex;align-items:center;font-size:11px}
.auction-links span{display:flex;align-items:center;gap:5px;padding:4px 9px 4px 0;border-right:1px solid var(--card-line);margin-right:9px}
.bid-btn{background:var(--green);color:var(--white);font-weight:700;font-size:10.5px;padding:7px 10px;border-radius:3px;border:1px solid var(--green-dark);white-space:nowrap}

/* sidebar */
.register{left:505px;top:426px;width:223px;height:74px;background:var(--green);border-radius:3px;color:var(--white)}
.register-icon{position:absolute;left:8px;top:10px}
.register-big{position:absolute;left:64px;top:8px;font-family:"Open Sans",sans-serif;font-weight:700;font-size:32px;line-height:1}
.register-small{position:absolute;left:65px;top:48px;font-size:14px;letter-spacing:.5px}
.widget{left:505px;width:222px;background:linear-gradient(#fafafa,#ececec);border:1px solid var(--card-line);border-radius:3px}
.widget-title{font-family:"Open Sans",sans-serif;font-weight:700;font-size:18px;color:var(--navy-text);letter-spacing:.3px;white-space:nowrap}
.signup{top:521px;height:115px;padding:10px 13px}
.signup p{font-size:10px;line-height:13px;margin-top:6px;color:var(--muted)}
.signup-form{display:flex;margin-top:7px}
.signup-input{width:160px;height:26px;border:1px solid #ccc;background:var(--white);font-size:9.5px;color:#888;padding:6px}
.signup-go{width:36px;height:26px;background:var(--green);color:var(--white);font-weight:700;font-size:13px;text-align:center;line-height:26px;border-radius:0 3px 3px 0}
.upcoming{top:656px;height:203px;padding:11px 14px}
.upcoming h4{font-size:10.5px;margin-top:11px;white-space:nowrap}
.upcoming-photo{width:188px;height:67px;margin:6px 0 10px;background:linear-gradient(180deg,#8fb2d6 0%,#c9c3b5 45%,#4d6d39 100%)}
.upcoming p{font-size:9.5px;line-height:12px;margin-bottom:6px}
.testimonials{top:880px;height:202px;padding:11px 13px}
.testimonials blockquote{position:relative;font-size:10px;line-height:14.8px;margin-top:12px;text-indent:26px}
.quote-mark{position:absolute;left:0;top:-4px;font-family:"Tinos",serif;font-size:34px;color:#aaa;line-height:1;text-indent:0}
.author{font-size:10px;font-weight:700;font-style:italic;color:var(--navy-text);margin-top:12px}

/* footer */
.footer-info{left:78px;top:1131px;color:#e6e7ee;font-size:10.5px;line-height:13.5px}
.footer-brand{left:384px;top:1143px;display:flex;align-items:center;gap:6px;color:var(--white);font-weight:700;font-size:16px}
.footer-brand .brand-mark{background:var(--white);width:10px;height:10px}
.badge{background:#f2f2f2}
</style>
</head>
<body>
<div class="page">
  <div class="abs brand">
    <div class="brand-mark"></div>
    <div>
      <div class="brand-name">BRIME</div>
      <div class="brand-sub">Realty &amp; Auction LLC</div>
    </div>
  </div>
  <div class="abs firm">FIRM # 4173</div>

  <div class="abs social">
    <span class="social-label">Social Media:</span>
    <span class="social-square sq-a" role="img" aria-label="Social network link"></span>
    <span class="social-square sq-b" role="img" aria-label="Social network link"></span>
    <span class="social-square sq-c" role="img" aria-label="Video channel link"></span>
  </div>
  <div class="abs contact">
    <svg width="13" height="13" viewBox="0 0 24 24"><path fill="#6a8c3f" d="M6.6 10.8a15 15 0 0 0 6.6 6.6l2.2-2.2c.3-.3.7-.4 1-.2 1.1.4 2.3.6 3.6.6.6 0 1 .4 1 1V20c0 .6-.4 1-1 1A17 17 0 0 1 3 4c0-.6.4-1 1-1h3.5c.6 0 1 .4 1 1 0 1.3.2 2.5.6 3.6.1.3 0 .7-.2 1z"/></svg>
    <span>(865) 555 0190</span>
    <svg width="16" height="11" viewBox="0 0 16 11" style="margin-left:6px"><rect width="16" height="11" fill="#6a8c3f"/><path d="M0 0l8 6 8-6" fill="none" stroke="#fff" stroke-width="1.3"/></svg>
    <span style="margin-left:4px">info@brimerealty.com</span>
  </div>

  <nav class="abs nav">
    <a href="#" style="width:64px">Home</a>
    <a href="#" class="active" style="width:119px">Current Auctions</a>
    <span class="spacer"></span>
    <a href="#" style="width:120px">Past Auctions</a>
    <a href="#" style="width:109px">Referrals</a>
    <a href="#" style="width:97px">Why Auction</a>
    <a href="#" style="width:88px">About Us</a>
    <a href="#" style="width:96px">Contact Us</a>
  </nav>

  <div class="abs hero" role="img" aria-label="Stock photo of a large country house with a green lawn"></div>
  <div class="abs tagline">Bid Bold With Brime!</div>

  <h1 class="abs welcome">Welcome to Brime Realty &amp; Auction LLC</h1>
  <p class="abs intro">simply dummy text of the printing and typesetting industry. Lorem Ipsum has been the industry's standard dummy text ever since the 1500s,</p>
  <h2 class="abs section-title">Current Auctions</h2>

  <article class="abs auction" style="top:531px">
    <h3 class="auction-title">Absolute Online Only Auction – Antiques &amp; Collectibles</h3>
    <div class="auction-photo" role="img" aria-label="Photo of a crowd gathered at a house auction"></div>
    <div class="auction-body">
      <div class="auction-kind">LIVE ON-SITE AUCTION</div>
      <p>Korvan BS3F High Lift, 600 Series Delmar tractor w/Hartline Loader, Dune buggy, 1207 RT Cutditioner: SHOP &amp;</p>
      <p><b>Begins:</b>&nbsp; Saturday, March 16, 2013 at 10:00 AM EDT</p>
      <p><b>Location:</b>&nbsp; 318 Alder Creek Road Maryville, TN 37801</p>
    </div>
    <div class="auction-links">
      <span><svg width="10" height="10" viewBox="0 0 10 10"><circle cx="4" cy="4" r="3" fill="none" stroke="#222" stroke-width="1.5"/><path d="M6 6l3.5 3.5" stroke="#222" stroke-width="1.8"/></svg>Details</span>
      <span><svg width="14" height="10" viewBox="0 0 14 10"><rect x=".5" y=".5" width="13" height="9" fill="none" stroke="#222"/><path d="M2 8l3-4 2 2 2-3 3 5z" fill="#222"/></svg>Gallery</span>
      <div class="bid-btn">Click here for our online Bidding site</div>
    </div>
  </article>

  <article class="abs auction" style="top:721px">
    <h3 class="auction-title">Absolute Online Only Auction – Antiques &amp; Collectibles</h3>
    <div class="auction-photo" role="img" aria-label="Photo of a crowd gathered at a house auction"></div>
    <div class="auction-body">
      <div class="auction-kind">LIVE ON-SITE AUCTION</div>
      <p>Korvan BS3F High Lift, 600 Series Delmar tractor w/Hartline Loader, Dune buggy, 1207 RT Cutditioner: SHOP &amp;</p>
      <p><b>Begins:</b>&nbsp; Saturday, March 16, 2013 at 10:00 AM EDT</p>
      <p><b>Location:</b>&nbsp; 318 Alder Creek Road Maryville, TN 37801</p>
    </div>
    <div class="auction-links">
      <span><svg width="10" height="10" viewBox="0 0 10 10"><circle cx="4" cy="4" r="3" fill="none" stroke="#222" stroke-width="1.5"/><path d="M6 6l3.5 3.5" stroke="#222" stroke-width="1.8"/></svg>Details</span>
      <span><svg width="14" height="10" viewBox="0 0 14 10"><rect x=".5" y=".5" width="13" height="9" fill="none" stroke="#222"/><path d="M2 8l3-4 2 2 2-3 3 5z" fill="#222"/></svg>Gallery</span>
      <div class="bid-btn">Click here for our online Bidding site</div>
    </div>
  </article>

  <article class="abs auction" style="top:913px;left:14px">
    <h3 class="auction-title">Absolute Online Only Auction – Antiques &amp; Collectibles</h3>
    <div class="auction-photo" role="img" aria-label="Photo of a crowd gathered at a house auction"></div>
    <div class="auction-body">
      <div class="auction-kind">LIVE ON-SITE AUCTION</div>
      <p>Korvan BS3F High Lift, 600 Series Delmar tractor w/Hartline Loader, Dune buggy, 1207 RT Cutditioner: SHOP &amp;</p>
      <p><b>Begins:</b>&nbsp; Saturday, March 16, 2013 at 10:00 AM EDT</p>
      <p><b>Location:</b>&nbsp; 318 Alder Creek Road Maryville, TN 37801</p>
    </div>
    <div class="auction-links">
      <span><svg width="10" height="10" viewBox="0 0 10 10"><circle cx="4" cy="4" r="3" fill="none" stroke="#222" stroke-width="1.5"/><path d="M6 6l3.5 3.5" stroke="#222" stroke-width="1.8"/></svg>Details</span>
      <span><svg width="14" height="10" viewBox="0 0 14 10"><rect x=".5" y=".5" width="13" height="9" fill="none" stroke="#222"/><path d="M2 8l3-4 2 2 2-3 3 5z" fill="#222"/></svg>Gallery</span>
      <div class="bid-btn">Click here for our online Bidding site</div>
    </div>
  </article>

  <aside>
    <div class="abs register">
      <svg class="register-icon" width="50" height="60" viewBox="0 0 50 60">
        <ellipse cx="22" cy="38" rx="17" ry="20" fill="#383c5c"/>
        <path d="M22 18v14M8 30h28" stroke="#6a8c3f" stroke-width="2"/>
        <path d="M24 18c4-10 14-8 20-16" fill="none" stroke="#383c5c" stroke-width="3"/>
      </svg>
      <div class="register-big">Register</div>
      <div class="register-small">for Online Bidding</div>
    </div>

    <section class="abs widget signup">
      <h3 class="widget-title">Email Sign Up</h3>
      <p>Sign up for our free messages &amp; receive auction alerts.</p>
      <div class="signup-form">
        <div class="signup-input">Your Email Address</div>
        <div class="signup-go">GO</div>
      </div>
    </section>

    <section class="abs widget upcoming">
      <h3 class="widget-title">Upcoming Auctions</h3>
      <h4>Multi Estate &amp; Consignment Auction</h4>
      <div class="upcoming-photo" role="img" aria-label="Photo of an agent in a suit in front of a suburban home"></div>
      <p><b>Start Date/ Time:</b> Saturday, April 13,<br>2013 At 10:00 Am</p>
      <p><b>Location:</b> 905 Quarry Lane,&nbsp; 37920</p>
    </section>

    <section class="abs widget testimonials">
      <h3 class="widget-title">Testimonials</h3>
      <blockquote><span class="quote-mark">&ldquo;</span>Lorem Ipsum has been the industry's standard dummy text ever since the 1500s, when an unknown printer took a galley of type and scrambled it to make a type speci men book.It has a galley of type and scrambled a galley of type and scrambled survived not only five centuries.</blockquote>
      <div class="author">-Mara Ellison</div>
    </section>
  </aside>
</div>

<footer>
  <div class="abs footer-info">
    Brime Realty &amp; Auction LLC.<br>
    4810 Harlow Ridge Rd., Knoxville TN 37918<br>
    office@brimerealty.com<br>
    Phone: (865) 555 0142
  </div>
  <div class="abs footer-brand"><span class="brand-mark"></span>BRIME</div>
  <div class="abs badge" style="left:538px;top:1146px;width:72px;height:36px" role="img" aria-label="Association badge"></div>
  <div class="abs badge" style="left:616px;top:1146px;width:45px;height:36px" role="img" aria-label="Association badge"></div>
  <div class="abs badge" style="left:666px;top:1146px;width:94px;height:36px" role="img" aria-label="Association badge"></div>
  <div class="abs badge" style="left:772px;top:1144px;width:36px;height:40px" role="img" aria-label="Association badge"></div>
</footer>
</body>
</html>
```